Business Card - connecting 2 souls and beggining the journey of self discovery

Logo on the front
with tag line

On the back list of services and contact details

Seminars
workshops
Coaching
podcasts

Daniel Porthwick
Health & Wellbeing Life Coach
0491 372 815
daniel@wovenpathwellness.example
wovenpathwellness.example

Industry/Entity Type

Life Coaching

Contact Information for Business Card

I like the use of colour from the logo to be used. I'm not a fan of white.

Requirements
Must have
• My tagline: The way back begins within you
Nice to have
• Use of colour that is in the mind body soul logo

```html
<!DOCTYPE html>
<html lang="en">
<head>
<meta charset="utf-8">
<title>Woven Path Wellness – Business Card</title>
<link rel="stylesheet" href="https://fonts.googleapis.com/css2?family=Montserrat:wght@500&family=Open+Sans:wght@600&family=Roboto:wght@400;500&family=Roboto+Condensed:wght@700&display=swap">
<style>
  :root {
    --backdrop: #2b2b2c;
    --card: #f1f1f1;
    --slate: #7d7e80;
    --ink-grey: #737476;
    --white: #ffffff;
    --teal: #2bb5a0;
    --green: #8cc63f;
    --coral: #ef5a6a;
    --orange: #f5923e;
    --violet: #8a3fb8;
    --mark: #ec6c5c;
  }
  * { margin: 0; padding: 0; box-sizing: border-box; }
  html, body { width: 1200px; height: 960px; overflow: hidden; }
  body { background: var(--backdrop); position: relative; }

  .card {
    position: absolute;
    width: 600px;
    height: 342px;
    background: var(--card);
    border-radius: 18px;
    overflow: hidden;
  }
  .card--front { left: 314px; top: 114px; }
  .card--back { left: 311px; top: 472px; }

  .wave { position: absolute; inset: 0; }

  .brand-mark {
    position: absolute;
    border-radius: 50%;
    background: var(--mark);
  }
  .card--front .brand-mark { left: 111px; top: 33px; width: 78px; height: 78px; }
  .card--back .brand-mark { left: 249px; top: 92px; width: 106px; height: 106px; }

  .brand-name {
    position: absolute;
    font-family: "Montserrat", sans-serif;
    font-weight: 500;
    color: var(--ink-grey);
    letter-spacing: -0.6px;
    white-space: nowrap;
  }
  .card--front .brand-name { left: 39px; top: 127px; font-size: 20px; }
  .card--back .brand-name { left: 0; width: 100%; top: 221px; font-size: 27px; text-align: center; }

  .tagline {
    position: absolute;
    left: 40px; top: 151px;
    font-family: "Open Sans", sans-serif;
    font-weight: 600;
    font-size: 13px;
    color: var(--ink-grey);
    white-space: nowrap;
  }

  .contact {
    position: absolute;
    right: 33px; top: 200px;
    text-align: right;
    color: var(--white);
    font-family: "Roboto", sans-serif;
  }
  .contact__name {
    font-family: "Roboto Condensed", sans-serif;
    font-weight: 700;
    font-size: 21px;
    line-height: 26px;
  }
  .contact__role {
    font-weight: 500;
    font-size: 14.5px;
    letter-spacing: 0.2px;
    line-height: 18px;
    margin-bottom: 12px;
  }
  .contact__line {
    display: flex;
    justify-content: flex-end;
    align-items: center;
    gap: 5px;
    font-size: 14.5px;
    line-height: 19px;
  }
  .contact__line svg { width: 13px; height: 13px; fill: var(--white); }

  .services {
    position: absolute;
    left: 0; top: 293px;
    width: 100%; height: 27px;
    background: var(--slate);
    color: var(--white);
    font-family: "Roboto", sans-serif;
    font-size: 14.5px;
    line-height: 27px;
    text-align: center;
  }
  .services .dot { font-size: 9px; padding: 0 2px; vertical-align: 1px; }
</style>
</head>
<body>

<section class="card card--front">
  <svg class="wave" width="600" height="342" viewBox="0 0 600 342" role="img" aria-label="Soft multicolour wave decoration above a grey panel">
    <defs>
      <linearGradient id="glow" x1="0" y1="0" x2="600" y2="0" gradientUnits="userSpaceOnUse">
        <stop offset="0" stop-color="var(--teal)"/>
        <stop offset="0.3" stop-color="var(--green)"/>
        <stop offset="0.5" stop-color="var(--orange)"/>
        <stop offset="0.75" stop-color="var(--coral)"/>
        <stop offset="1" stop-color="var(--violet)"/>
      </linearGradient>
    </defs>
    <path class="wave__glow" fill="url(#glow)" opacity="0.35"
      d="M0,212 C60,242 130,270 190,262 C260,252 330,152 400,102 C460,62 520,50 600,64 L600,342 L0,342 Z"/>
    <path class="wave__fill" fill="var(--slate)"
      d="M0,232 C60,262 130,290 190,282 C260,272 330,172 400,122 C460,82 520,70 600,84 L600,342 L0,342 Z"/>
  </svg>

  <div class="brand-mark" aria-hidden="true"></div>
  <div class="brand-name">Woven Path Wellness</div>
  <div class="tagline">The way back begins within you</div>

  <div class="contact">
    <div class="contact__name">DANIEL PORTHWICK</div>
    <div class="contact__role">HEALTH &amp; WELLBEING LIFE COACH</div>
    <div class="contact__line">0491 372 815
      <svg viewBox="0 0 16 16" aria-hidden="true"><path d="M3.5 1.5l2.3-.4 1.3 3.2-1.5 1.2a9 9 0 0 0 4.9 4.9l1.2-1.5 3.2 1.3-.4 2.3c-.2.8-.9 1.3-1.7 1.2C7 12.9 3.1 9 2.3 3.2c-.1-.8.4-1.5 1.2-1.7z"/></svg>
    </div>
    <div class="contact__line">daniel@wovenpathwellness.example
      <svg viewBox="0 0 16 16" aria-hidden="true"><path d="M1 3h14v1.2L8 8.6 1 4.2z M1 5.6l7 4.4 7-4.4V13H1z"/></svg>
    </div>
    <div class="contact__line">www.wovenpathwellness.example
      <svg viewBox="0 0 16 16" aria-hidden="true"><path d="M8 1a7 7 0 1 0 0 14A7 7 0 0 0 8 1zm-1 2.2v2.2L5 7.5 3.2 6.6A5 5 0 0 1 7 3.2zm1.5 10.2V11l2-2-1.5-2 2-1.5.9-1.6a5 5 0 0 1-3.4 9.5z"/></svg>
    </div>
  </div>
</section>

<section class="card card--back">
  <div class="brand-mark" aria-hidden="true"></div>
  <div class="brand-name">Woven Path Wellness</div>
  <div class="services">
    Seminars <span class="dot">●</span> Workshops <span class="dot">●</span> Coaching <span class="dot">●</span> Podcasts
  </div>
</section>

</body>
</html>
```